A social health network MOBILE APP needs an awesome home page

We need a home page design that is attractive, and simple to navigate for our mobile app. This app helps people maintain their personal health records, find and connect with care providers to ask question, get care online or face to face through appointment. It also has a few other features to encourage engagement such as Forum, Reward, Service Discount Coupon.
We would like to see the design that uses the color green (our company color) as the main color, and includes an area for announcement plus another area for advertising. We include sketches of our need for your review.
The final design should look modern, friendly, and lively.
Updates
If possible, please break away from our attached sketch format and let your creativity leads the way? We would like to see the bottom buttons layout in differently from the sketch.
Industry/Entity Type
Health
Colors
Designer to choose colors to be used in the design.
Requirements
Must have
- A clean and elegant look.

```html
<!DOCTYPE html>
<html lang="en">
<head>
<meta charset="utf-8">
<title>Health Network App – Home</title>
<link href="https://fonts.googleapis.com/css2?family=Roboto:wght@400;500;700&display=swap" rel="stylesheet">
<style>
:root{
  --stage:#dcdcdc;
  --green:#34b93a;
  --green-dark:#2ea633;
  --green-band:#3fae3e;
  --ink:#2b2b2b;
  --icon:#555555;
  --white:#ffffff;
  --bubble:#e9e9e9;
  --tabbar:#333333;
  --tab-muted:#9a9a9a;
  --promo-orange:#f0892a;
  --brand-red:#e0201c;
}
*{box-sizing:border-box;margin:0;padding:0}
html,body{width:1200px;height:1200px;overflow:hidden;background:var(--stage);font-family:"Roboto",Arial,sans-serif;color:var(--ink)}
.canvas{position:relative;width:1200px;height:1200px;overflow:hidden}
.screen{position:absolute;overflow:hidden;background:var(--white)}
.screen--home{left:61px;top:289px;width:460px;height:911px}
.screen--scrolled{left:615px;top:0;width:459px;height:762px}

.status-bar{position:absolute;left:0;top:0;width:100%;height:25px;background:var(--green);color:var(--white);font-size:14px;font-weight:500;display:flex;align-items:center;justify-content:space-between;padding:0 14px 0 10px;white-space:nowrap}
.status-bar .battery{display:inline-block;width:26px;height:11px;border:1.5px solid var(--white);border-radius:2px;vertical-align:middle;margin-left:4px;position:relative}
.status-bar .battery::after{content:"";position:absolute;inset:1px;right:2px;background:var(--white)}

.hero{position:absolute;left:0;top:25px;width:100%;height:240px;background:linear-gradient(120deg,#6b4a34 0%,#a27c5c 30%,#d9d2c8 55%,#8d8a72 80%,#5a6a4c 100%)}
.hero__caption{position:absolute;left:0;bottom:0;width:100%;height:54px;background:rgba(70,150,60,.72);color:var(--white);font-size:23px;line-height:21px;text-align:center;padding-top:6px}
.carousel-dots{position:absolute;left:0;top:265px;width:100%;height:26px;background:var(--green-band);display:flex;justify-content:center;align-items:center;gap:16px}
.carousel-dots span{width:11px;height:11px;border-radius:50%;background:var(--white)}
.carousel-dots span.is-active{background:#2f8a2f}

.quick-actions{position:absolute;left:0;top:291px;width:100%;height:170px;background:var(--green)}
.quick-action{position:absolute;top:30px;width:130px;margin-left:-65px;text-align:center;color:var(--white);font-weight:700;font-size:15px;white-space:nowrap}
.quick-action__bubble{width:84px;height:84px;border-radius:50%;background:var(--bubble);margin:0 auto 18px;display:flex;align-items:center;justify-content:center;border:3px solid rgba(255,255,255,.5)}
.quick-action__bubble svg{width:44px;height:44px;fill:var(--green)}

.divider{position:absolute;left:0;width:100%;height:6px;background:#e6e6e6}

.feature-grid{position:absolute;left:0;width:100%;height:408px;background:var(--white)}
.feature{position:absolute;width:150px;margin-left:-75px;text-align:center;font-size:18px;color:var(--ink);white-space:nowrap}
.feature svg{display:block;margin:0 auto 6px;width:64px;height:64px;fill:var(--icon)}

.promo{position:absolute;left:0;width:100%;overflow:hidden;background:linear-gradient(100deg,#7f9a68 0%,#b9c7a3 35%,#d8cfc3 60%,#a6b58c 100%)}
.promo__brand{position:absolute;left:12px;top:10px;font-size:30px;font-weight:700;color:var(--brand-red);letter-spacing:-.5px;white-space:nowrap}
.promo__tagline{position:absolute;left:176px;top:24px;font-size:10px;color:rgba(255,255,255,.85);text-transform:uppercase;white-space:nowrap}
.promo__offer{position:absolute;right:0;top:55px;width:110px;height:203px;background:var(--promo-orange);clip-path:polygon(100% 0,100% 100%,0 100%,0 70%)}
.promo__discount{position:absolute;right:18px;top:142px;font-size:38px;color:var(--white)}
.promo__note{position:absolute;right:20px;top:188px;width:84px;font-size:8.5px;line-height:11px;color:var(--white);text-align:center}
.promo__badge{position:absolute;right:18px;top:228px;width:58px;height:20px;border-radius:3px;background:rgba(255,255,255,.85)}
.promo__dots{position:absolute;left:178px;top:230px;display:flex;gap:18px}
.promo__dots span{width:9px;height:9px;border-radius:50%;background:rgba(255,255,255,.85)}
.promo__dots span.is-active{background:var(--green)}

.top-strip{position:absolute;left:0;top:0;width:100%;height:26px;background:var(--green);color:var(--white);font-weight:700;font-size:15px}
.top-strip span{position:absolute;top:-9px;transform:translateX(-50%);white-space:nowrap}

.tab-bar{position:absolute;left:0;top:696px;width:100%;height:66px;background:var(--tabbar);border-top:3px solid #4a4a4a}
.tab{position:absolute;top:8px;width:92px;margin-left:-46px;text-align:center;color:var(--tab-muted);font-size:14px;white-space:nowrap}
.tab svg{display:block;margin:0 auto 2px;width:34px;height:34px;fill:none;stroke:var(--tab-muted);stroke-width:2.4}
.tab.is-active{color:var(--white)}
.tab.is-active svg{stroke:var(--white)}
</style>
</head>
<body>
<svg width="0" height="0" style="position:absolute" aria-hidden="true">
  <defs>
    <symbol id="i-forum" viewBox="0 0 64 64"><path d="M4 6h38v26H16l-8 7v-7H4z"/><path d="M46 18h6v32l-8-6H20v-8h26z"/><rect x="52" y="18" width="6" height="28"/></symbol>
    <symbol id="i-connections" viewBox="0 0 64 64"><g fill="none" stroke="currentColor" stroke-width="6"><circle cx="32" cy="15" r="10"/><circle cx="13" cy="48" r="10"/><circle cx="51" cy="48" r="10"/><path d="M27 24l-9 15M37 24l9 15M23 48h18"/></g></symbol>
    <symbol id="i-invite" viewBox="0 0 64 64"><circle cx="28" cy="16" r="14"/><path d="M4 60c0-18 10-26 24-26 8 0 14 3 18 8-6 2-10 8-10 14v4z"/><path d="M48 44h5v7h7v5h-7v7h-5v-7h-7v-5h7z"/></symbol>
    <symbol id="i-rewards" viewBox="0 0 64 64"><rect x="20" y="2" width="24" height="6" rx="2"/><path d="M24 10h16l-4 8h-8z"/><path d="M26 20h12c14 8 22 20 22 30 0 8-6 12-14 12H18C10 62 4 58 4 50c0-10 8-22 22-30z"/><text x="32" y="52" font-family="Roboto,Arial,sans-serif" font-size="26" font-weight="700" text-anchor="middle" fill="#fff">$</text></symbol>
    <symbol id="i-coupons" viewBox="0 0 64 64"><rect x="14" y="16" width="46" height="40" rx="4" fill="none" stroke="currentColor" stroke-width="5"/><rect x="22" y="24" width="30" height="24" fill="none" stroke="currentColor" stroke-width="2.5" stroke-dasharray="4 3"/><circle cx="10" cy="10" r="7" fill="none" stroke="currentColor" stroke-width="4"/><circle cx="10" cy="30" r="7" fill="none" stroke="currentColor" stroke-width="4"/><path d="M15 14l28 14M15 26l28-14" stroke="currentColor" stroke-width="4"/></symbol>
    <symbol id="i-scan" viewBox="0 0 64 64"><path d="M4 4h14v5H9v9H4zM46 4h14v14h-5V9h-9zM4 46h5v9h9v5H4zM55 46h5v14H46v-5h9z"/><rect x="16" y="16" width="6" height="32"/><rect x="27" y="20" width="4" height="8"/><rect x="27" y="36" width="4" height="8"/><rect x="35" y="16" width="5" height="32"/><rect x="44" y="16" width="5" height="32"/></symbol>
    <symbol id="i-info" viewBox="0 0 64 64"><path d="M32 2a29 29 0 0 1 8 57l-8 8-8-8A29 29 0 0 1 32 2z"/><circle cx="32" cy="31" r="23" fill="#fff"/><circle cx="32" cy="18" r="4"/><path d="M26 26h9v16h4v4H25v-4h4V30h-3z"/></symbol>
  </defs>
</svg>

<main class="canvas">

  <section class="screen screen--home" style="color:var(--icon)">
    <div class="status-bar"><span>▪︎ Carrier Wi-Fi</span><span>9:54 AM</span><span>91% <i class="battery"></i></span></div>
    <div class="hero" role="img" aria-label="Photo of a smiling woman looking at her phone on a sunny street">
      <p class="hero__caption">In just few seconds you can<br>get results</p>
    </div>
    <div class="carousel-dots"><span class="is-active"></span><span></span><span></span><span></span><span></span></div>

    <nav class="quick-actions">
      <div class="quick-action" style="left:96px">
        <div class="quick-action__bubble"><svg viewBox="0 0 48 48"><rect x="8" y="6" width="32" height="38" rx="3"/><rect x="17" y="2" width="14" height="8" rx="2" fill="#fff"/><path d="M15 26l6 6 12-13" fill="none" stroke="#fff" stroke-width="4"/></svg></div>Records
      </div>
      <div class="quick-action" style="left:243px">
        <div class="quick-action__bubble"><svg viewBox="0 0 48 48"><path d="M12 36a10 10 0 0 1-1-20 14 14 0 0 1 27 2 9 9 0 0 1-1 18z"/><text x="24" y="33" font-family="Roboto,Arial,sans-serif" font-size="22" font-weight="700" text-anchor="middle" fill="#fff">?</text><circle cx="24" cy="42" r="3"/></svg></div>Questions
      </div>
      <div class="quick-action" style="left:390px">
        <div class="quick-action__bubble"><svg viewBox="0 0 48 48"><path d="M24 4a14 14 0 0 1 14 14c0 10-14 26-14 26S10 28 10 18A14 14 0 0 1 24 4z"/><circle cx="24" cy="18" r="5" fill="#fff"/></svg></div>Find service
      </div>
    </nav>

    <div class="divider" style="top:461px"></div>

    <section class="feature-grid" style="top:467px">
      <div class="feature" style="left:83px;top:48px"><svg><use href="#i-forum"/></svg>Forum</div>
      <div class="feature" style="left:230px;top:48px"><svg style="color:var(--icon)"><use href="#i-connections"/></svg>Connections</div>
      <div class="feature" style="left:377px;top:48px"><svg><use href="#i-invite"/></svg>Invite</div>
      <div class="feature" style="left:83px;top:176px"><svg><use href="#i-rewards"/></svg>Rewards</div>
      <div class="feature" style="left:230px;top:176px"><svg style="color:var(--icon)"><use href="#i-coupons"/></svg>Coupons</div>
      <div class="feature" style="left:377px;top:176px"><svg><use href="#i-scan"/></svg>Scan Voucher</div>
      <div class="feature" style="left:230px;top:296px"><svg><use href="#i-info"/></svg>Info</div>
    </section>

    <aside class="promo" style="top:875px;height:258px" role="img" aria-label="Advertisement photo of a grandparent family with nutritional shake products">
      <span class="promo__brand">Vita Blend</span>
      <span class="promo__tagline">Ultra premium nutritional shake mix</span>
    </aside>
  </section>

  <section class="screen screen--scrolled" style="color:var(--icon)">
    <div class="top-strip">
      <span style="left:84px">Records</span><span style="left:228px">Questions</span><span style="left:378px">Find service</span>
    </div>
    <div class="divider" style="top:26px;height:4px"></div>

    <section class="feature-grid" style="top:30px">
      <div class="feature" style="left:83px;top:50px"><svg><use href="#i-forum"/></svg>Forum</div>
      <div class="feature" style="left:227px;top:50px"><svg><use href="#i-connections"/></svg>Connections</div>
      <div class="feature" style="left:377px;top:50px"><svg><use href="#i-invite"/></svg>Invite</div>
      <div class="feature" style="left:83px;top:178px"><svg><use href="#i-rewards"/></svg>Rewards</div>
      <div class="feature" style="left:227px;top:178px"><svg><use href="#i-coupons"/></svg>Coupons</div>
      <div class="feature" style="left:377px;top:178px"><svg><use href="#i-scan"/></svg>Scan Voucher</div>
      <div class="feature" style="left:230px;top:300px"><svg><use href="#i-info"/></svg>Info</div>
    </section>

    <aside class="promo" style="top:438px;height:258px">
      <div role="img" aria-label="Advertisement photo of grandparents playing with their granddaughter beside nutritional shake products" style="position:absolute;inset:0"></div>
      <span class="promo__brand">Vita Blend</span>
      <span class="promo__tagline">Ultra premium nutritional shake mix</span>
      <div class="promo__offer"></div>
      <span class="promo__discount">-25%</span>
      <span class="promo__note">+ Free shipping on all orders this month</span>
      <span class="promo__badge"></span>
      <div class="promo__dots"><span></span><span></span><span class="is-active"></span><span></span></div>
    </aside>

    <nav class="tab-bar">
      <div class="tab is-active" style="left:46px"><svg viewBox="0 0 34 34"><path d="M5 16L17 5l12 11v14H5z"/></svg>Home</div>
      <div class="tab" style="left:138px"><svg viewBox="0 0 34 34"><circle cx="8" cy="27" r="3" fill="#9a9a9a"/><path d="M5 16a13 13 0 0 1 13 13M5 8a21 21 0 0 1 21 21"/></svg>Feed</div>
      <div class="tab" style="left:230px"><svg viewBox="0 0 34 34"><path d="M9 24V15a8 8 0 0 1 16 0v9l3 3H6zM14 29a3 3 0 0 0 6 0"/></svg>Notification</div>
      <div class="tab" style="left:321px"><svg viewBox="0 0 34 34"><rect x="4" y="8" width="26" height="18" rx="2"/><path d="M4 9l13 10 13-10"/></svg>Message</div>
      <div class="tab" style="left:414px"><svg viewBox="0 0 34 34"><circle cx="17" cy="17" r="5"/><circle cx="17" cy="17" r="11" stroke-dasharray="5 3"/></svg>Settings</div>
    </nav>
  </section>

</main>
</body>
</html>
```